I need a business card design for my new clinic (SPORTS MEDICINE OF KNEE). I am orthopedist, expert in sports surgery, especially knee surgery. I prefer, as colors, the colors of my logo (green, black and white). I already have my logo and should appear on my card. It's good to see my site to have ideas (www.drlucianovarela.com)
It needs contain:
my name: Dr. Luciano Varela
my registration: CRM 584-902
my specialty: Cirurgia do Joelho / Esporte
my address: Centro Executivo - Pinheiral Plaza
Av. Doutor Augusto Brandão Cunha, 2740 sala 0836
Jd. Ipanema - Ribeirão Preto - SP
my phone number: Tel (16) 8245-3908
my clinic phone: (16) 3670-4851
my e-mail: drlucianovarela@mailbox-exemplo.com
my site: www.drlucianovarela.com

Target Market(s)

futures patients

Industry/Entity Type

Clinic

Requirements
Nice to have
• letters not overfilled
straight lines, with few curves

```html
<!DOCTYPE html>
<html lang="pt-BR">
<head>
<meta charset="utf-8">
<title>Varela – Cartão de Visita</title>
<link rel="stylesheet" href="https://fonts.googleapis.com/css2?family=Lato:wght@400;700&display=swap">
<style>
  :root {
    --green: #157a5c;
    --green-light: #3fae78;
    --charcoal: #48474a;
    --ink: #1d1d1d;
    --paper: #ffffff;
    --text-grey: #3c3c3c;
    --backdrop: #eceae6;
  }
  * { box-sizing: border-box; margin: 0; padding: 0; }
  html, body { width: 1200px; height: 1000px; overflow: hidden; }
  body {
    background: var(--backdrop);
    font-family: "Lato", sans-serif;
    position: relative;
  }
  .card {
    position: absolute;
    top: 355px;
    width: 560px;
    height: 290px;
    border-radius: 9px;
    overflow: hidden;
    background: var(--paper);
    box-shadow: 0 6px 16px rgba(0,0,0,0.25);
  }
  .card--front { left: 25px; }
  .card--back { left: 615px; }

  .brand {
    position: absolute;
    display: flex;
    align-items: center;
    gap: 14px;
  }
  .brand__square {
    width: 50px; height: 50px;
    background: var(--green-light);
    border-radius: 4px;
  }
  .brand__name {
    font-size: 42px;
    font-weight: 400;
    color: var(--ink);
    letter-spacing: 1px;
    line-height: 1;
  }

  /* front */
  .card--front .brand { left: 50%; top: 58px; transform: translateX(-50%); }
  .front__band { position: absolute; left: 0; top: 175px; width: 100%; height: 30px; background: var(--green); }
  .front__lower { position: absolute; left: 0; top: 205px; width: 100%; height: 85px; background: var(--charcoal); }
  .front__notch { position: absolute; left: 102px; top: 204px; }
  .doctor { position: absolute; left: 27px; top: 223px; color: var(--paper); }
  .doctor__name { font-size: 21px; font-weight: 700; margin-left: 6px; }
  .doctor__specialty { font-size: 15px; margin-top: 9px; }
  .contacts { position: absolute; left: 282px; top: 214px; list-style: none; color: var(--paper); }
  .contacts li { display: flex; align-items: center; gap: 7px; height: 22px; font-size: 15px; }
  .contacts .contacts__email { font-size: 12.5px; }
  .icon { width: 16px; height: 16px; flex: none; }

  /* back */
  .back__top { position: absolute; left: 0; top: 0; width: 100%; height: 28px; background: var(--green); }
  .back__notch { position: absolute; left: 262px; top: 27px; }
  .back__bottom { position: absolute; left: 0; bottom: 0; width: 100%; height: 27px; background: var(--green); }
  .card--back .brand { left: 50%; top: 92px; transform: translateX(-50%); }
  .address { position: absolute; left: 18px; top: 198px; font-size: 12.5px; line-height: 17px; color: var(--text-grey); font-style: normal; }
  .clinic-phone { position: absolute; left: 362px; top: 200px; display: flex; align-items: center; gap: 10px; font-size: 17px; color: var(--text-grey); }
  .clinic-phone .icon { width: 20px; height: 20px; }
  .registration { position: absolute; left: 362px; top: 233px; font-size: 12.5px; color: var(--text-grey); }
</style>
</head>
<body>

<section class="card card--front" aria-label="Frente do cartão">
  <div class="brand">
    <span class="brand__square"></span>
    <span class="brand__name">VARELA</span>
  </div>
  <div class="front__band"></div>
  <div class="front__lower"></div>
  <svg class="front__notch" width="36" height="18" viewBox="0 0 36 18"><polygon points="0,0 36,0 18,18" fill="#157a5c"/></svg>

  <div class="doctor">
    <p class="doctor__name">Dr. Luciano Varela</p>
    <p class="doctor__specialty">Cirurgia do Joelho / Esporte</p>
  </div>

  <ul class="contacts">
    <li>
      <svg class="icon" viewBox="0 0 16 16"><circle cx="8" cy="8" r="7.3" fill="none" stroke="#fff" stroke-width="1.2"/><path d="M5.3 4.2l1.4-.3.8 1.9-.9.7c.5 1.1 1.3 1.9 2.3 2.4l.7-.9 1.9.8-.3 1.4c-3.2.1-6.2-2.9-6.2-6z" fill="#fff"/></svg>
      Tel (16) 8245-3908
    </li>
    <li class="contacts__email">
      <svg class="icon" viewBox="0 0 16 16"><circle cx="8" cy="8" r="7.3" fill="none" stroke="#fff" stroke-width="1.2"/><rect x="4" y="5.2" width="8" height="5.6" fill="#fff"/><path d="M4 5.2l4 3 4-3" fill="none" stroke="#48474a" stroke-width="0.9"/></svg>
      drlucianovarela@mailbox-exemplo.com
    </li>
    <li>
      <svg class="icon" viewBox="0 0 16 16" fill="none" stroke="#fff" stroke-width="1.1"><circle cx="8" cy="8" r="7.2"/><ellipse cx="8" cy="8" rx="3" ry="7.2"/><path d="M1 8h14M2.2 4.6h11.6M2.2 11.4h11.6"/></svg>
      www.drlucianovarela.com
    </li>
  </ul>
</section>

<section class="card card--back" aria-label="Verso do cartão">
  <div class="back__top"></div>
  <svg class="back__notch" width="36" height="18" viewBox="0 0 36 18"><polygon points="0,0 36,0 18,18" fill="#157a5c"/></svg>
  <div class="brand">
    <span class="brand__square"></span>
    <span class="brand__name">VARELA</span>
  </div>

  <address class="address">
    Centro Executivo - Pinheiral Plaza<br>
    Av. Doutor Augusto Brandão Cunha, 2740<br>
    sala 0836 Jd. Ipanema - Ribeirão Preto - SP
  </address>

  <div class="clinic-phone">
    <svg class="icon" viewBox="0 0 16 16"><circle cx="8" cy="8" r="7.2" fill="none" stroke="#3c3c3c" stroke-width="1.2"/><path d="M5.3 4.2l1.4-.3.8 1.9-.9.7c.5 1.1 1.3 1.9 2.3 2.4l.7-.9 1.9.8-.3 1.4c-3.2.1-6.2-2.9-6.2-6z" fill="#3c3c3c"/></svg>
    (16) 3670-4851
  </div>
  <p class="registration">registration: CRM 584-902</p>

  <div class="back__bottom"></div>
</section>

</body>
</html>
```